Upmarket building and construction company needs signage

Our building company R Brent Construction, needs signage to put up on the side of our vehicle trailers and on site fencing. We are a building company that specialises in residential construction and carpentry .

I will attach our logo and some inspirational pics for site fencing as well as what our trailer looks like .
Other details i would like on the sign are our
( email) rbrentconstruction@mailbox-example.net
(mobile ) 0493 518 264
(website ) rbrentconstruction. example.net

Target Market(s)

Home owners looking for a reliable local builder who produces good quality work. I have attached some inspirational pics.

Industry/Entity Type

Building and Construction

Colors

Designer to choose colors to be used in the design.

Requirements
Must have
• Our logo, contact information
Nice to have
• We would like the design to have elements of being Elegant, Serious, Modern, Professional, Masculine, Conservative and Upmarket.

```html
<!DOCTYPE html>
<html lang="en">
<head>
<meta charset="utf-8">
<title>R Brent Construction – Site Signage</title>
<link href="https://fonts.googleapis.com/css2?family=Jost:wght@300;400&display=swap" rel="stylesheet">
<style>
  :root {
    --page: #ffffff;
    --panel: #343841;
    --ink: #ffffff;
    --shadow: rgba(0, 0, 0, 0.28);
  }
  * { margin: 0; padding: 0; box-sizing: border-box; }
  html, body {
    width: 1200px;
    height: 1200px;
    overflow: hidden;
    background: var(--page);
  }
  .canvas {
    position: relative;
    width: 1200px;
    height: 1200px;
    background: var(--page);
  }
  .sign {
    position: absolute;
    left: 61px;
    top: 112px;
    width: 1078px;
    height: 418px;
    background: var(--panel);
    box-shadow: 0 -14px 40px var(--shadow), 0 10px 30px rgba(0,0,0,0.12);
    color: var(--ink);
    font-family: "Jost", sans-serif;
  }
  .brand {
    position: absolute;
    left: 159px;
    top: 108px;
    width: 270px;
  }
  .brand-square {
    width: 38px;
    height: 38px;
    background: var(--ink);
    margin: 0 0 22px auto;
  }
  .brand-name {
    font-weight: 300;
    color: var(--ink);
    line-height: 1;
  }
  .brand-name .line-main {
    display: block;
    font-size: 62px;
    letter-spacing: 3px;
  }
  .brand-name .line-sub {
    display: block;
    font-size: 29px;
    letter-spacing: 2.6px;
    margin-top: 10px;
  }
  .brand-tagline {
    margin-top: 10px;
    font-size: 16px;
    font-weight: 300;
    letter-spacing: 1.2px;
  }
  .contacts {
    position: absolute;
    left: 514px;
    top: 140px;
    list-style: none;
  }
  .contact {
    display: flex;
    align-items: center;
    height: 40px;
    margin-bottom: 17px;
    font-weight: 400;
    font-size: 25px;
    letter-spacing: 0.4px;
  }
  .contact--phone { font-size: 31px; letter-spacing: 1px; }
  .contact-icon {
    width: 36px;
    height: 36px;
    margin-right: 20px;
    flex: none;
  }
</style>
</head>
<body>
<div class="canvas">
  <section class="sign">
    <div class="brand">
      <div class="brand-square"></div>
      <div class="brand-name">
        <span class="line-main">R BRENT</span>
        <span class="line-sub">CONSTRUCTION</span>
      </div>
      <div class="brand-tagline">BUILDING AND CARPENTRY</div>
    </div>

    <ul class="contacts">
      <li class="contact contact--phone">
        <svg class="contact-icon" viewBox="0 0 36 36" aria-hidden="true">
          <path d="M9 4l5 7-3 3c1.5 4 5 7.5 9 9l3-3 7 5-3 5c-10 1-22-11-21-21z" fill="#fff"/>
          <path d="M20 9a8 8 0 0 1 7 7M20 4a13 13 0 0 1 12 12" stroke="#fff" stroke-width="2.4" fill="none" stroke-linecap="round"/>
        </svg>
        <span>0493 518 264</span>
      </li>
      <li class="contact contact--web">
        <svg class="contact-icon" viewBox="0 0 36 36" aria-hidden="true">
          <circle cx="18" cy="18" r="16" fill="#fff"/>
          <path d="M10 8c4 1 6 4 4 7s-6 2-6 6 4 3 4 7M22 6c-2 3 1 5 4 5s4 4 2 6-5 1-5 5 2 6 4 7" stroke="#343841" stroke-width="3" fill="none" stroke-linecap="round"/>
        </svg>
        <span>rbrentconstruction. example.net</span>
      </li>
      <li class="contact contact--email">
        <svg class="contact-icon" viewBox="0 0 36 36" aria-hidden="true">
          <rect x="1" y="7" width="34" height="22" fill="#fff"/>
          <path d="M2 9l16 12 16-12" stroke="#343841" stroke-width="2.6" fill="none"/>
        </svg>
        <span>rbrentconstruction@mailbox-example.net</span>
      </li>
    </ul>
  </section>
</div>
</body>
</html>
```